business card and flyer/pricelist

Business Name: Willow Strand Salon
new boutique salon run from home, using Australian owned natural products and colours, we need a flyer design to do a letter box drop to advertise the business as well as incorporating a price list on the front (single sided with writing on front and only colour on back)

The salon has a natural feel with light coloured timber chairs, bamboo timber bench top and shelving.

we are after a natural toned colour for the flyer, with possibly a brown/darkish colour writing

we are after a flyer that will also be able to use the design heading (business name) for business cards as well

feel free to look on my pintrest account to get a feel for my style under Corinne Belvane.

I love simple clean and Natural looks.

Industry/Entity Type

Boutique

Font styles to use
Script
Other font styles liked:
• SCRIPT HANDWRITTEN FONTS

Colors
cadf82
e9f1ce
5c5c5c
d3d3d3
add136
fee18a

Requirements
Must have
• NATURAL COLOURINGS, eg soft greens, browns,
white or off white background.
Should not have
• photos,

```html
<!DOCTYPE html>
<html lang="en">
<head>
<meta charset="utf-8">
<title>Willow Strand Salon – Flyer and Price List</title>
<link href="https://fonts.googleapis.com/css2?family=Great+Vibes&family=Lora:ital,wght@1,400;1,600&family=PT+Sans:wght@400;700&display=swap" rel="stylesheet">
<style>
  :root{
    --stage:#ededed;
    --paper:#d3d3d3;
    --charcoal:#5c5c5c;
    --leaf:#add136;
    --bark:#5a1e14;
    --ink:#6b2a1c;
    --mist:#e9e9e9;
    --white:#ffffff;
  }
  *{box-sizing:border-box;margin:0;padding:0}
  html,body{width:1200px;height:1200px;overflow:hidden}
  body{background:var(--stage);position:relative;font-family:"Lora",Georgia,serif}

  .flyer{position:absolute;top:170px;width:400px;height:860px;overflow:hidden;background:var(--paper);box-shadow:0 4px 14px rgba(0,0,0,.18)}
  .flyer--front{left:180px}
  .flyer--back{left:620px}
  .flyer__shapes{position:absolute;inset:0;width:400px;height:860px}

  .brand{position:absolute;color:var(--mist);transform:rotate(90deg);transform-origin:center;text-align:right;white-space:nowrap}
  .brand__name{font-family:"Great Vibes",cursive;font-weight:400;line-height:1}
  .brand__sub{font-family:"Great Vibes",cursive;line-height:1}
  .flyer--front .brand{left:140px;top:200px;width:380px}
  .flyer--front .brand__name{font-size:60px}
  .flyer--front .brand__sub{font-size:26px;margin-top:2px;padding-right:12px}
  .flyer--back .brand{left:-180px;top:380px;width:600px}
  .flyer--back .brand__name{font-size:88px}
  .flyer--back .brand__sub{font-size:36px;margin-top:4px;padding-right:20px}

  .pricelist{position:absolute;left:24px;top:44px;width:158px;color:var(--ink);font-style:italic}
  .pricelist__heading{font-size:18px;font-weight:400;margin:8px 0 2px}
  .pricelist__heading:first-child{margin-top:0}
  .price-row{display:flex;align-items:baseline;font-size:12.5px;line-height:16px;font-weight:600}
  .price-row__leader{flex:1;border-bottom:1.5px dotted var(--ink);margin:0 4px;min-width:8px;transform:translateY(-3px)}
  .price-row__note{font-size:12px;line-height:15px;font-weight:600}

  .contact{position:absolute;left:228px;top:512px;width:170px;color:var(--mist);font-size:12px;line-height:16px}
  .contact__line{display:flex;align-items:flex-start;gap:6px;margin-bottom:6px}
  .contact__icon{flex:none;width:11px;height:11px;margin-top:2px}

  .offer{position:absolute;left:0;top:664px;width:400px;text-align:center;font-family:"PT Sans",Arial,sans-serif;font-weight:700;text-transform:uppercase}
  .offer__special{color:var(--leaf);font-size:30px;line-height:30px;letter-spacing:.5px}
  .offer__line{color:var(--white);font-size:14px;line-height:17px}
  .offer__amount{color:var(--leaf);font-size:32px;vertical-align:-4px}
  .offer__rule{width:110px;height:1px;background:var(--white);margin:6px auto 4px;position:relative}
  .offer__visit{color:var(--leaf);font-size:19px;line-height:22px}

  .partners{position:absolute;left:12px;top:806px;width:322px;height:40px;background:var(--white);border-radius:3px;display:flex;align-items:center;justify-content:space-around;font-family:"PT Sans",Arial,sans-serif;font-weight:700;font-size:12px;color:var(--charcoal)}
  .socials{position:absolute;left:340px;top:806px;width:48px;height:40px;display:flex;flex-direction:column;align-items:center;justify-content:center;gap:2px;font-family:"PT Sans",Arial,sans-serif;font-weight:700;font-size:9px;color:var(--white)}
  .socials__mark{width:20px;height:20px;background:var(--leaf)}
</style>
</head>
<body>

<section class="flyer flyer--front" aria-label="Flyer front with price list">
  <svg class="flyer__shapes" viewBox="0 0 400 860" aria-hidden="true">
    <circle cx="432" cy="270" r="246" fill="var(--bark)"/>
    <circle cx="436" cy="270" r="243" fill="var(--leaf)"/>
    <circle cx="446" cy="270" r="238" fill="var(--charcoal)"/>
    <rect x="216" y="500" width="200" height="74" rx="14" fill="var(--charcoal)"/>
    <circle cx="200" cy="1052" r="410" fill="var(--bark)"/>
    <circle cx="200" cy="1054" r="404" fill="var(--leaf)"/>
    <circle cx="200" cy="1062" r="404" fill="var(--charcoal)"/>
  </svg>

  <div class="brand">
    <div class="brand__name">Willow Strand</div>
    <div class="brand__sub">salon</div>
  </div>

  <div class="pricelist">
    <h3 class="pricelist__heading">Cuts</h3>
    <div class="price-row"><span>Ladies (inc. shampoo/ blowdry)</span><span class="price-row__leader"></span><span>$45</span></div>
    <div class="price-row"><span>Mens</span><span class="price-row__leader"></span><span>$20</span></div>
    <div class="price-row"><span>13 &amp; Under From</span><span class="price-row__leader"></span><span>$15</span></div>
    <div class="price-row"><span>5 &amp; Under</span><span class="price-row__leader"></span><span>$10</span></div>

    <h3 class="pricelist__heading">Blowdry &amp; Styling</h3>
    <div class="price-row"><span>Short</span><span class="price-row__leader"></span><span>$25</span></div>
    <div class="price-row"><span>Medium</span><span class="price-row__leader"></span><span>$30</span></div>
    <div class="price-row"><span>Long</span><span class="price-row__leader"></span><span>$40</span></div>
    <div class="price-row"><span>Straight Iron (after blowdry)</span><span class="price-row__leader"></span><span>$10</span></div>
    <div class="price-row"><span>Upstyles</span><span class="price-row__leader"></span><span>POA</span></div>
    <div class="price-row"><span>Onsite styling</span><span class="price-row__leader"></span><span>$55</span></div>

    <h3 class="pricelist__heading">Colours</h3>
    <div class="price-row"><span>Regrowth</span><span class="price-row__leader"></span><span>$55</span></div>
    <div class="price-row"><span>Short</span><span class="price-row__leader"></span><span>$60</span></div>
    <div class="price-row"><span>Medium</span><span class="price-row__leader"></span><span>$75</span></div>
    <div class="price-row"><span>Long</span><span class="price-row__leader"></span><span>$85</span></div>

    <h3 class="pricelist__heading">Foils</h3>
    <div class="price-row"><span>Top Foils</span><span class="price-row__leader"></span><span>$95</span></div>
    <div class="price-row"><span>½ head</span><span class="price-row__leader"></span><span>$110</span></div>
    <div class="price-row"><span>Full head</span><span class="price-row__leader"></span><span>$145</span></div>
    <div class="price-row__note">(all include toner)</div>

    <h3 class="pricelist__heading">Treatments</h3>
    <div class="price-row"><span>At basin</span><span class="price-row__leader"></span><span>$35</span></div>
    <div class="price-row"><span>Special Feet From</span><span class="price-row__leader"></span><span>$10</span></div>
    <div class="price-row__note">Eye brow/lash treatments</div>
  </div>

  <address class="contact" style="font-style:italic">
    <div class="contact__line">
      <svg class="contact__icon" viewBox="0 0 12 12" aria-hidden="true"><circle cx="6" cy="6" r="5.5" fill="var(--mist)"/><path d="M6 2.5a2 2 0 0 0-2 2c0 1.6 2 4 2 4s2-2.4 2-4a2 2 0 0 0-2-2z" fill="var(--bark)"/></svg>
      <span>18 Banksia Lane<br>Greenvale</span>
    </div>
    <div class="contact__line">
      <svg class="contact__icon" viewBox="0 0 12 12" aria-hidden="true"><circle cx="6" cy="6" r="5.5" fill="var(--mist)"/><rect x="4.2" y="2.6" width="3.6" height="6.8" rx=".8" fill="var(--bark)"/></svg>
      <span>0412 555 087</span>
    </div>
  </address>

  <div class="offer">
    <div class="offer__special">Special</div>
    <div class="offer__line">Introductory offer -</div>
    <div class="offer__line">Receive <span class="offer__amount">25%off</span></div>
    <div class="offer__rule"></div>
    <div class="offer__visit">Your initial visit</div>
  </div>

  <div class="partners">
    <span>Fernleaf</span>
    <span>CardPay</span>
    <span>TapCard</span>
    <span>PayLink</span>
  </div>
  <div class="socials">
    <span class="socials__mark"></span>
    <span>Socials</span>
  </div>
</section>

<section class="flyer flyer--back" aria-label="Flyer back">
  <svg class="flyer__shapes" viewBox="0 0 400 860" aria-hidden="true">
    <circle cx="-40" cy="437" r="324" fill="var(--bark)"/>
    <circle cx="-46" cy="437" r="322" fill="var(--leaf)"/>
    <circle cx="-58" cy="437" r="320" fill="var(--charcoal)"/>
  </svg>
  <div class="brand">
    <div class="brand__name">Willow Strand</div>
    <div class="brand__sub">salon</div>
  </div>
</section>

</body>
</html>
```